'Private English tutoring'

I need a flyer design to advertise private English tutoring. I am offering lessons to ethnic minority groups in my local area in south Belfast. The biggest ethnic minorities groups are Chinese, Polish and Indian and African. I can teach at any level, from beginner English to advanced. The tutoring will be either one on one or small groups of four students. I can teach adults and children but my preference would be to teach adults.

The flyer would need to be easily understood by people who have English as a second language.

I am also offering proof reading and editing services to students at local universities and colleges.

Target Market(s)

Adults of ethnic minorities who may not speak or read much English

Industry/Entity Type

Tutoring

Font styles to use
Serif

Requirements
Must have
• It needs to communicate that I am an accredited TEFL (Teaching English as a Foreign language) tutor with 2 years experience and that I tutor Beginners - Advanced students. It would also need to say that I offer proof reading and editing services. It would also need to communicate the cost of lessons are £15, but there are group rates for groups of 2-4 students. It would need to include my contact details which are as follows: contact Mona Hargrove BTh at 07812609354 or email monahargroveenglish@quillpost.com
Nice to have
• In terms of design I would like it to be warm and inviting and something which would convey an atmosphere of learning for non English speakers. Other than that I don't have any preferences.
Should not have
• Nothing which is going to be offensive to ethnic minorities.
• No pictures of people

```html
<!DOCTYPE html>
<html lang="en">
<head>
<meta charset="utf-8">
<title>Private English Tutoring</title>
<link href="https://fonts.googleapis.com/css2?family=Comic+Neue:wght@400;700&display=swap" rel="stylesheet">
<style>
  :root {
    --wood-light: #e6c894;
    --wood-mid: #d2ab6c;
    --wood-dark: #b88b4c;
    --board-light: #5a8a68;
    --board-mid: #4a7a58;
    --board-dark: #3a6548;
    --chalk: #f6f7f0;
    --band: #ffffff;
    --band-text: #3f6d4d;
    --page: #2a2a2a;
  }
  * { margin: 0; padding: 0; box-sizing: border-box; }
  html, body {
    width: 1200px; height: 845px; overflow: hidden;
    background: var(--page);
  }
  .flyer {
    position: relative;
    width: 1200px; height: 845px;
    font-family: "Comic Neue", "Comic Sans MS", cursive;
    font-weight: 700;
    color: var(--chalk);
  }
  .frame {
    position: absolute; inset: 0;
    background: linear-gradient(135deg, var(--wood-light), var(--wood-mid) 55%, var(--wood-dark));
  }
  .board {
    position: absolute; left: 38px; top: 36px; right: 38px; bottom: 36px;
    background: radial-gradient(ellipse at 40% 35%, var(--board-light), var(--board-mid) 55%, var(--board-dark));
    box-shadow: inset 0 0 30px rgba(0,0,0,0.35);
  }
  .decor { position: absolute; inset: 0; width: 1200px; height: 845px; }
  .text { position: absolute; line-height: 1; white-space: nowrap; }

  .heading { left: 0; width: 1200px; text-align: center; top: 77px; font-size: 40px; letter-spacing: 1px; }
  .headline { left: 100px; top: 160px; font-size: 76px; }
  .subline { left: 102px; top: 250px; font-size: 47px; letter-spacing: 0.5px; }

  .band {
    position: absolute; left: 38px; top: 336px; width: 780px; height: 46px;
    background: var(--band);
  }
  .band-text { left: 102px; top: 342px; font-size: 33px; color: var(--band-text); }

  .tutor-lead { left: 104px; top: 412px; font-size: 27px; font-weight: 400; }
  .tutor-years { left: 104px; top: 443px; font-size: 37px; font-weight: 400; letter-spacing: 0.5px; }
  .tutor-levels { left: 104px; top: 487px; font-size: 27px; font-weight: 400; }

  .offer-title { left: 838px; top: 348px; width: 290px; text-align: center; font-size: 44px; font-weight: 400; }
  .offer-body { left: 838px; top: 397px; width: 290px; text-align: center; font-size: 27px; line-height: 1.05; white-space: normal; }

  .price { left: 320px; top: 537px; font-size: 26px; }
  .price-amount { font-size: 40px; vertical-align: -3px; }
  .groups { left: 0; width: 1010px; text-align: center; top: 579px; font-size: 26px; }

  .contact-label { left: 318px; top: 653px; font-size: 26px; font-weight: 400; }
  .contact-name { left: 100px; top: 682px; font-size: 27px; }
  .contact-phone { left: 492px; top: 644px; font-size: 76px; letter-spacing: 1px; }
  .contact-email { left: 100px; top: 744px; font-size: 32px; }

  .chalk-stick {
    position: absolute; left: 1020px; top: 793px; width: 68px; height: 12px;
    background: var(--chalk); border-radius: 3px;
  }
</style>
</head>
<body>
<main class="flyer">
  <div class="frame"></div>
  <div class="board"></div>

  <svg class="decor" viewBox="0 0 1200 845" aria-hidden="true">
    <line x1="96" y1="141" x2="1093" y2="141" stroke="#f6f7f0" stroke-width="3"/>
    <line x1="96" y1="626" x2="1093" y2="626" stroke="#f6f7f0" stroke-width="3"/>
    <ellipse cx="983" cy="418" rx="146" ry="86" fill="none" stroke="#f6f7f0" stroke-width="5"/>
    <path d="M915 494 L985 560" fill="none" stroke="#f6f7f0" stroke-width="5" stroke-linecap="round"/>
    <path d="M400 696 H448 M434 684 L449 696 L434 708" fill="none" stroke="#f6f7f0" stroke-width="3" stroke-linecap="round" stroke-linejoin="round"/>
  </svg>

  <h1 class="text heading">PRIVATE ENGLISH TUTORING</h1>
  <p class="text headline">Communicate</p>
  <p class="text subline">That I am an accredited TEFL</p>

  <div class="band"></div>
  <p class="text band-text">Teaching English as a Foreign language</p>

  <p class="text tutor-lead">Tutor with</p>
  <p class="text tutor-years">2 YEARS EXPERIENCE</p>
  <p class="text tutor-levels">and that I tutor Beginners Advanced students</p>

  <p class="text offer-title">OFFER</p>
  <p class="text offer-body">Proof Reading<br>and Editing<br>Services</p>

  <p class="text price">Communicate the cost of Lessons are <span class="price-amount">£15</span></p>
  <p class="text groups">Groups of 2-4 Students</p>

  <p class="text contact-label">Contact</p>
  <p class="text contact-name">Mona Hargrove BTh</p>
  <p class="text contact-phone">07812609354</p>
  <p class="text contact-email">or email monahargroveenglish@quillpost.com</p>

  <div class="chalk-stick"></div>
</main>
</body>
</html>
```